Energy Company needs a Business Card Design

We need a business card design for a new company based in Singapore called Tarn Energy. Tarn Energy is a producer of renewable energies largely for the biofuels market. Sourced entirely from sustainable resources, Tarn Energy aims to be a fully integrated oil company operating in 100% sustainable way. We would like to see designs that use the same colours as the attached file.

Industry/Entity Type

Business

```html
<!DOCTYPE html>
<html lang="en">
<head>
<meta charset="UTF-8">
<title>Tarn Energy — Business Cards</title>
<link rel="stylesheet" href="https://fonts.googleapis.com/css2?family=Montserrat:wght@400;500;700&display=swap">
<style>
  :root {
    --backdrop: #d8d7d3;
    --card-white: #ffffff;
    --card-black: #1f1f1f;
    --leaf-green: #8cc63f;
    --ink-dark: #3a3a3a;
    --wordmark-silver: #a9abae;
  }
  * { box-sizing: border-box; margin: 0; padding: 0; }
  html, body {
    width: 1200px;
    height: 900px;
    overflow: hidden;
    background: var(--backdrop);
    font-family: "Montserrat", sans-serif;
  }
  .canvas {
    position: relative;
    width: 1200px;
    height: 900px;
  }
  .card {
    position: absolute;
    width: 560px;
    height: 320px;
    box-shadow: 0 6px 18px rgba(0,0,0,0.18);
  }
  .card--logo-white { left: 320px; top: 100px; background: var(--card-white); }
  .card--logo-black { left: 40px; top: 480px; background: var(--card-black); }
  .card--contact {
    left: 600px; top: 480px;
    background: var(--card-white);
    border-left: 4px solid var(--leaf-green);
  }

  .brand {
    position: absolute;
    inset: 0;
    display: flex;
    align-items: center;
    justify-content: center;
    gap: 16px;
  }
  .brand__dot {
    width: 22px;
    height: 22px;
    border-radius: 50%;
    background: var(--leaf-green);
  }
  .brand__name {
    font-weight: 500;
    font-size: 46px;
    letter-spacing: 3px;
    text-transform: uppercase;
    color: var(--wordmark-silver);
  }

  .contact {
    position: absolute;
    left: 100px;
    top: 48px;
    right: 30px;
  }
  .contact__name {
    font-weight: 700;
    font-size: 26px;
    letter-spacing: 1px;
    color: var(--leaf-green);
  }
  .contact__title {
    font-size: 16px;
    letter-spacing: 1.5px;
    color: var(--ink-dark);
    margin-top: 2px;
  }
  .contact__address {
    font-size: 17px;
    letter-spacing: 1.5px;
    line-height: 1.3;
    color: var(--ink-dark);
    margin-top: 30px;
  }
  .contact__list {
    list-style: none;
    margin-top: 12px;
  }
  .contact__item {
    display: flex;
    align-items: center;
    gap: 12px;
    font-size: 17px;
    letter-spacing: 1px;
    line-height: 1.45;
    color: var(--ink-dark);
  }
  .contact__icon {
    width: 18px;
    height: 18px;
    flex: none;
  }
</style>
</head>
<body>
<main class="canvas">

  <section class="card card--logo-white" aria-label="Card front, white">
    <div class="brand">
      <span class="brand__dot"></span>
      <span class="brand__name">Tarn Energy</span>
    </div>
  </section>

  <section class="card card--logo-black" aria-label="Card front, black">
    <div class="brand">
      <span class="brand__dot"></span>
      <span class="brand__name">Tarn Energy</span>
    </div>
  </section>

  <section class="card card--contact" aria-label="Card back, contact details">
    <div class="contact">
      <p class="contact__name">Marcus Lee</p>
      <p class="contact__title">President</p>
      <p class="contact__address">48 Harbour Lane<br>Singapore 049321</p>
      <ul class="contact__list">
        <li class="contact__item">
          <svg class="contact__icon" viewBox="0 0 18 18" aria-hidden="true">
            <circle cx="9" cy="9" r="9" fill="#8cc63f"/>
            <rect x="6.2" y="4" width="5.6" height="10" rx="1" fill="#fff"/>
            <rect x="7.2" y="5.2" width="3.6" height="6" fill="#8cc63f"/>
          </svg>
          +65. 6123. 4580
        </li>
        <li class="contact__item">
          <svg class="contact__icon" viewBox="0 0 18 18" aria-hidden="true">
            <circle cx="9" cy="9" r="9" fill="#8cc63f"/>
            <path d="M5.5 5 L7.5 4.6 L8.4 7 L7.2 8 Q8 10 10 10.8 L11 9.6 L13.4 10.5 L13 12.5 Q8 13 5.5 8 Z" fill="#fff"/>
          </svg>
          +65. 9234. 5671
        </li>
        <li class="contact__item">
          <svg class="contact__icon" viewBox="0 0 18 18" aria-hidden="true">
            <circle cx="9" cy="9" r="9" fill="#8cc63f"/>
            <rect x="4.5" y="5.8" width="9" height="6.4" fill="#fff"/>
            <path d="M4.5 5.8 L9 9.4 L13.5 5.8" fill="none" stroke="#8cc63f" stroke-width="1"/>
          </svg>
          info@tarnenergy.com
        </li>
        <li class="contact__item">
          <svg class="contact__icon" viewBox="0 0 18 18" aria-hidden="true">
            <circle cx="9" cy="9" r="9" fill="#8cc63f"/>
            <g fill="none" stroke="#fff" stroke-width="1.1">
              <circle cx="9" cy="9" r="4.8"/>
              <ellipse cx="9" cy="9" rx="2" ry="4.8"/>
              <line x1="4.2" y1="9" x2="13.8" y2="9"/>
            </g>
          </svg>
          www.tarnenergy.com
        </li>
      </ul>
    </div>
  </section>

</main>
</body>
</html>
```